Marigold's Lantern - Foundation PPT

Design a cohesive, emotionally resonant PowerPoint template that reflects the heart of Marigold’s Lantern Pregnancy & Family Support. This template will be used across fundraising, partnership, and storytelling presentations, and must balance professionalism with warmth, compassion, and human connection.

Background
Marigold’s Lantern Pregnancy & Family Support exists to support families navigating complicated pregnancies, prolonged hospital stays, and loss. The brand is rooted in empathy, quiet strength, and the concept of a “web” of care—an interconnected support system that surrounds families during difficult moments.

The template should feel deeply personal and mission-driven, not corporate.

Design Goals
Create a visually cohesive slide system that can be reused across multiple presentation types

Capture the emotional tone of the organization:
-Warm
-Gentle
-Hopeful
-Supportive
Ensure the design is clean, minimal, and easy to use for non-designers
Maintain a balance between storytelling and credibility

Key Design Requirements
-Brand Integration: Incorporate the Marigold’s Lantern logo (provided)
Align with soft, neutral color palette (e.g., cream, sage, blush, light sky tones)
-Use elegant, readable typography

Slide Templates to Include
-Cover Slide (emotion-forward, minimal text)
-Mission / Story Slide
-Program Overview Slide
-Impact / Metrics Slide
-Partnership / Sponsor Slide
-“Web of Support” Concept Slide (visual representation of interconnected care)
-Call to Action Slide
-Optional: Quote/Testimonial Slide

Visual Style
-Soft, calming, and approachable aesthetic
-Use of whitespace to avoid clutter
-Light use of icons or illustrations (if applicable)
-Avoid overly corporate or overly busy design elements

Usability
-Fully editable in PowerPoint
-Clear text hierarchy and placeholders
-Easy for internal team to update content without design support
-Tone & Emotional Direction

This is not a clinical or corporate presentation—it should feel human, heartfelt, and intentional.

website: https://www.marigoldslanterncare.org

```html
<!DOCTYPE html>
<html lang="en">
<head>
<meta charset="utf-8">
<title>Marigold's Lantern - Foundation Presentation Template</title>
<link href="https://fonts.googleapis.com/css2?family=Playfair+Display:ital,wght@0,400;0,500;0,600;0,700;1,400&family=Poppins:ital,wght@0,300;0,400;0,500;0,600;0,700;1,300;1,400&display=swap" rel="stylesheet">
<style>
:root{
  --page:#e3e3e3;
  --cream:#faf5f2;
  --ink:#2b2230;
  --body:#5a5158;
  --muted:#6d6870;
  --purple:#9a6fa5;
  --purple-deep:#9458ab;
  --rose:#b98584;
  --sage:#737f6c;
  --teal:#6b929c;
  --teal-soft:#7598a0;
  --chip:#6e7868;
  --white:#ffffff;
}
*{margin:0;padding:0;box-sizing:border-box}
html,body{width:1005px;height:1200px;overflow:hidden}
body{background:var(--page);font-family:"Poppins",sans-serif;color:var(--ink);position:relative}
.slide{position:absolute;width:443px;height:249px;background:var(--cream);overflow:hidden;box-shadow:0 1px 3px rgba(0,0,0,.08)}
.s1{left:49px;top:46px;background:var(--teal)}
.s2{left:520px;top:49px}
.s3{left:42px;top:334px}
.s4{left:520px;top:334px}
.s5{left:42px;top:619px}
.s6{left:520px;top:619px}
.s7{left:42px;top:905px}
.s8{left:520px;top:905px;background:radial-gradient(circle at 50% 45%,#a366b6 0%,var(--purple-deep) 70%)}

.accent{position:absolute;left:0;top:6px;width:5px;height:20px;background:var(--purple);border-radius:0 2px 2px 0}
.slide-title{position:absolute;left:20px;top:6px;font-family:"Playfair Display",serif;font-weight:600;font-size:15px;line-height:20px;color:var(--ink);display:flex;align-items:center;gap:6px;white-space:nowrap}
.slide-title .lead{color:var(--purple);font-weight:500}
.slide-title .dot{width:9px;height:9px;border-radius:50%;background:var(--purple);opacity:.8}

.footer{position:absolute;left:20px;right:20px;bottom:8px;height:12px;display:flex;align-items:center;justify-content:space-between}
.footer .url{font-size:7.2px;color:var(--muted)}
.footer .brand{position:absolute;left:177px;font-size:5.2px;font-weight:500;color:var(--purple);white-space:nowrap}
.footer .page-no{width:11px;height:10px;border-radius:2px;background:var(--chip);color:var(--white);font-size:5px;font-weight:600;display:flex;align-items:center;justify-content:center}

.photo{position:absolute}

/* cover */
.cover-shape{position:absolute;inset:0}
.cover-brand{position:absolute;left:19px;top:38px;display:flex;align-items:center;gap:5px;color:var(--white);font-size:11px;font-weight:400;white-space:nowrap}
.cover-brand .mark{width:10px;height:10px;border-radius:50%;border:1px solid var(--white)}
.cover-title{position:absolute;left:19px;top:82px;width:210px;font-family:"Playfair Display",serif;font-weight:500;font-size:20px;line-height:28px;color:var(--white)}
.cover-rule{position:absolute;left:20px;top:170px;width:49px;height:2px;background:#c98a88}
.cover-sub{position:absolute;left:20px;top:186px;font-size:7.6px;color:var(--white);white-space:nowrap}
.cover-tags{position:absolute;left:20px;top:203px;font-size:5.6px;color:var(--white)}
.cover-photo{left:239px;top:32px;width:185px;height:185px;border-radius:0 30px 0 30px;background:linear-gradient(135deg,#8a6a52 0%,#d9b59a 55%,#e8d6c8 100%)}

/* story */
.story-text{position:absolute;left:230px;top:42px;width:194px}
.story-text .intro{font-size:6.9px;line-height:12.6px;color:var(--ink);margin-bottom:6px}
.story-text p{font-size:5.7px;line-height:11.5px;color:var(--body);text-align:justify;margin-bottom:2px}

/* programs */
.programs{position:absolute;left:19px;top:53px;display:flex;gap:5px}
.program{width:97px;height:138px;border-radius:10px;color:var(--white);text-align:center;padding-top:10px}
.program.rose{background:var(--rose)}
.program.purple{background:var(--purple)}
.program.sage{background:var(--sage)}
.program.teal{background:var(--teal)}
.program .icon{width:32px;height:32px;margin:0 auto;border-radius:50%;background:var(--white);display:flex;align-items:center;justify-content:center}
.program h3{font-size:6.2px;font-weight:500;margin-top:11px;letter-spacing:.1px}
.program p{font-size:5.8px;line-height:11.5px;margin-top:6px;padding:0 8px;opacity:.95}

/* impact */
.impact-sub{position:absolute;left:20px;top:48px;font-size:7.6px;font-weight:500;color:var(--ink)}
.impact-body{position:absolute;left:20px;top:64px;width:178px;font-size:6.1px;line-height:11.5px;color:var(--body);text-align:justify}
.stats{position:absolute;left:75px;top:147px;display:flex;gap:9px}
.stat{width:92px;height:61px;border-radius:9px;color:var(--white);text-align:center;padding-top:9px;box-shadow:0 3px 6px rgba(0,0,0,.12)}
.stat.sage{background:var(--sage)}
.stat.purple{background:var(--purple)}
.stat.rose{background:var(--rose)}
.stat .num{font-family:"Playfair Display",serif;font-size:21px;line-height:24px;font-weight:400}
.stat .label{font-size:5.4px;margin-top:5px}

/* quote */
.quote-box{position:absolute;left:19px;top:45px;width:404px;height:161px;border-radius:22px;background:var(--teal-soft);text-align:center;color:var(--white)}
.quote-box .mark{font-family:"Playfair Display",serif;font-size:96px;line-height:96px;color:var(--purple);font-weight:700;margin-top:2px;height:48px;overflow:visible}
.quote-box .lede{font-size:7.6px;line-height:13.5px;font-style:italic;font-weight:300;margin-top:10px}
.quote-box blockquote{font-size:13.6px;line-height:20.5px;font-style:italic;font-weight:300;margin-top:5px}
.quote-box cite{display:block;font-style:normal;font-weight:600;font-size:8.2px;margin-top:5px;letter-spacing:.3px}

/* call to action */
.cta-name{position:absolute;left:19px;top:53px;font-size:15.4px;font-weight:600;color:var(--rose);white-space:nowrap}
.cta-head{position:absolute;left:19px;top:73px;width:200px;font-size:15.4px;line-height:20.5px;font-weight:600;color:var(--ink)}
.cta-tag{position:absolute;left:20px;top:126px;font-size:6px;color:var(--ink)}
.cta-button{position:absolute;left:19px;top:150px;width:122px;height:32px;border-radius:16px;background:var(--purple);color:var(--white);font-size:9.6px;font-weight:600;display:flex;align-items:center;justify-content:center}

/* closing */
.close-brand{position:absolute;left:0;right:0;top:78px;display:flex;align-items:center;justify-content:center;gap:7px;color:var(--white);font-size:17px;font-weight:400}
.close-brand .mark{width:13px;height:13px;border-radius:50%;border:1.2px solid var(--white)}
.close-title{position:absolute;left:0;right:0;top:123px;text-align:center;font-family:"Playfair Display",serif;font-weight:700;font-size:34px;color:var(--white)}
</style>
</head>
<body>

<!-- Cover -->
<section class="slide s1">
  <svg class="cover-shape" viewBox="0 0 443 249" preserveAspectRatio="none" aria-hidden="true">
    <path d="M294 0 H443 V249 H327 V110 C327 50 320 12 294 0 Z" fill="#9a6fa5"/>
    <path d="M294 0 C320 12 327 50 327 110 V249 H321 V110 C321 52 314 16 288 0 Z" fill="#bf8a8c"/>
  </svg>
  <div class="cover-brand"><span class="mark"></span>Marigold’s Lantern</div>
  <h1 class="cover-title">Holding Families Through The Hardest Moments</h1>
  <div class="cover-rule"></div>
  <div class="cover-sub">Marigold’s Lantern Pregnancy &amp; Family Support</div>
  <div class="cover-tags">Fundraising • Partnerships • Impact</div>
  <div class="photo cover-photo" role="img" aria-label="Photo of a smiling pregnant mother and her young daughter at home"></div>
</section>

<!-- Our Story -->
<section class="slide s2">
  <div class="accent"></div>
  <h2 class="slide-title"><span><span class="lead">Our</span> Story</span><span class="dot"></span></h2>
  <div class="photo" role="img" aria-label="Photo of a pregnant woman in conversation with a caregiver"
       style="left:20px;top:40px;width:183px;height:169px;border-radius:0 24px 0 24px;background:linear-gradient(135deg,#4e5a55,#b8b4a6 55%,#dcd6cc)"></div>
  <div class="story-text">
    <div class="intro">Marigold’s Lantern was created from lived experience and a deep calling to support families during moments of profound uncertainty.</div>
    <p>Marigold’s story is woven into the very foundation of this work. During a complicated pregnancy marked by prolonged hospital stays, unanswered questions, and long stretches of waiting, our family experienced firsthand how isolating this season can feel. Even with excellent medical care, there were moments when support felt fragmented when emotional weight, practical needs, and financial uncertainty all collided at once.</p>
    <p>Marigold was lovingly known as our little sunshine.In a moment filled with so much pain, when we were finally able to see her tiny hands, her feet, her nose, her lips.</p>
  </div>
  <div class="footer"><span class="url">www.marigoldslanterncare.org</span><span class="brand">Marigold’s Lantern</span><span class="page-no">02</span></div>
</section>

<!-- Programs -->
<section class="slide s3">
  <div class="accent"></div>
  <h2 class="slide-title"><span><span class="lead">How We</span> Support Families</span><span class="dot"></span></h2>
  <div class="programs">
    <div class="program rose">
      <div class="icon"><svg width="16" height="16" viewBox="0 0 24 24"><path d="M12 21s-8-5.2-8-11a4.5 4.5 0 0 1 8-2.8A4.5 4.5 0 0 1 20 10c0 5.8-8 11-8 11z" fill="#e0404b"/></svg></div>
      <h3>EMOTIONAL SUPPORT</h3>
      <p>Lorem ipsum dolor sit amet, consectetur adip-iscing elit, sed do eiusmod tempor incididunt ut labore et dolore</p>
    </div>
    <div class="program purple">
      <div class="icon"><svg width="16" height="16" viewBox="0 0 24 24"><path d="M12 17s-6-3.8-6-8a3.3 3.3 0 0 1 6-2 3.3 3.3 0 0 1 6 2c0 4.2-6 8-6 8z" fill="#e0404b"/><path d="M11 7.5h2v2h2v2h-2v2h-2v-2H9v-2h2z" fill="#fff"/><path d="M3 19c3-1 5 1 9 1s6-2 9-3" stroke="#5aa9d6" stroke-width="1.6" fill="none"/></svg></div>
      <h3>HOSPITAL SUPPORT</h3>
      <p>Lorem ipsum dolor sit amet, consectetur adip-iscing elit, sed do eiusmod tempor incididunt ut labore et dolore</p>
    </div>
    <div class="program sage">
      <div class="icon"><svg width="16" height="16" viewBox="0 0 24 24"><path d="M12 20s-7-4.5-7-9.5a3.8 3.8 0 0 1 7-2.3 3.8 3.8 0 0 1 7 2.3c0 5-7 9.5-7 9.5z" fill="#d99a7a"/><path d="M18 4.5s-2-1.3-2-2.6a1 1 0 0 1 2-.6 1 1 0 0 1 2 .6c0 1.3-2 2.6-2 2.6z" fill="#e0404b"/></svg></div>
      <h3>LOSS &amp; GRIEF CARE</h3>
      <p>Lorem ipsum dolor sit amet, consectetur adip-iscing elit, sed do eiusmod tempor incididunt ut labore et dolore</p>
    </div>
    <div class="program teal">
      <div class="icon"><svg width="18" height="18" viewBox="0 0 24 24"><circle cx="12" cy="4" r="2" fill="#e0404b"/><circle cx="20" cy="12" r="2" fill="#3b8fd6"/><circle cx="12" cy="20" r="2" fill="#f2b233"/><circle cx="4" cy="12" r="2" fill="#4cb56a"/><path d="M12 15s-3.5-2.2-3.5-4.6a1.9 1.9 0 0 1 3.5-1 1.9 1.9 0 0 1 3.5 1C15.5 12.8 12 15 12 15z" fill="#e0404b"/></svg></div>
      <h3>COMMUNITY CONNECTION</h3>
      <p>Lorem ipsum dolor sit amet, consectetur adip-iscing elit, sed do eiusmod tempor incididunt ut labore et dolore</p>
    </div>
  </div>
  <div class="footer"><span class="url">www.marigoldslanterncare.org</span><span class="brand">Marigold’s Lantern</span><span class="page-no">03</span></div>
</section>

<!-- Impact -->
<section class="slide s4">
  <div class="accent"></div>
  <h2 class="slide-title"><span><span class="lead">Our</span> Impact</span><span class="dot"></span></h2>
  <div class="impact-sub">A Web of Support—When It’s Needed Most</div>
  <p class="impact-body">We provide emotional and practical support to families navigating complex pregnancies and loss. Through care packages, shared stories, and connection, we aim to bring comfort, dignity, and community during life’s most difficult moments.</p>
  <div class="photo" role="img" aria-label="Photo of a mother resting with her newborn in a hospital bed"
       style="left:222px;top:37px;width:202px;height:95px;border-radius:10px;background:linear-gradient(120deg,#5c6a6e,#b9a6a2 50%,#e3c6cc)"></div>
  <div class="stats">
    <div class="stat sage"><div class="num">100+</div><div class="label">Families Supported</div></div>
    <div class="stat purple"><div class="num">250+</div><div class="label">Care Packages Delivered</div></div>
    <div class="stat rose"><div class="num">3M</div><div class="label">Moments of Support</div></div>
  </div>
  <div class="footer"><span class="url">www.marigoldslanterncare.org</span><span class="brand">Marigold’s Lantern</span><span class="page-no">04</span></div>
</section>

<!-- Testimonial -->
<section class="slide s5">
  <div class="accent"></div>
  <h2 class="slide-title"><span><span class="lead">Stories</span> of Love, Loss, and Strength</span><span class="dot"></span></h2>
  <div class="quote-box">
    <div class="mark">“</div>
    <p class="lede">Behind every diagnosis, every loss, and every moment of uncertainty<br>is a story filled with love, hope, and deep courage.</p>
    <blockquote>"Woven with care, held with hope, and touched<br>by a little sunshine."</blockquote>
    <cite>- RENATA MOSS</cite>
  </div>
  <div class="footer"><span class="url">www.marigoldslanterncare.org</span><span class="brand">Marigold’s Lantern</span><span class="page-no">05</span></div>
</section>

<!-- Blank content -->
<section class="slide s6">
  <div class="accent"></div>
  <h2 class="slide-title"><span><span class="lead">Title</span> Goes Here</span><span class="dot"></span></h2>
  <div class="footer"><span class="url">www.marigoldslanterncare.org</span><span class="brand">Marigold’s Lantern</span><span class="page-no">06</span></div>
</section>

<!-- Call to action -->
<section class="slide s7">
  <div class="accent"></div>
  <h2 class="slide-title"><span><span class="lead">Title</span> Goes Here</span><span class="dot"></span></h2>
  <div class="cta-name">Marigold’s Lantern</div>
  <div class="cta-head">Pregnancy and Family Support</div>
  <div class="cta-tag">A web of care for every family who needs it</div>
  <div class="cta-button">Support A Family</div>
  <div class="photo" role="img" aria-label="Photo of a pregnant woman receiving an ultrasound with a caregiver and a supporter beside her"
       style="left:221px;top:29px;width:222px;height:180px;border-radius:24px 0 0 24px;background:linear-gradient(135deg,#d8d2d6,#8e7c7a 50%,#4f5b78)"></div>
  <div class="footer"><span class="url">www.marigoldslanterncare.org</span><span class="brand">Marigold’s Lantern</span><span class="page-no">07</span></div>
</section>

<!-- Closing -->
<section class="slide s8">
  <div class="close-brand"><span class="mark"></span>Marigold’s Lantern</div>
  <div class="close-title">Thanking You!</div>
</section>

</body>
</html>
```